WordPress Site Clean up

We are a small wireless networking company in Norther Colorado. We have a basic layout to our new website, and require a person or persons who can clean the new site up so we can go live with it in the coming weeks. Our company has the logo and content, we just need to clean the formatting up, improve the colors/graphics. It is currently a ZUNPLIKE. We also need help making our project pictures look better on the website, and clean up the images all around.

The website can be found at: www.4qvtelmora.com/newsite

We can provide you with photos and more content, but we have gone as far as we can with "building" the wordpress site.

It Company

```html
<!DOCTYPE html>
<html lang="en">
<head>
<meta charset="utf-8">
<title>Velnar Networks</title>
<link href="https://fonts.googleapis.com/css2?family=Open+Sans:wght@400;600;700&display=swap" rel="stylesheet">
<style>
:root{
  --green:#8dc63f;
  --green-dark:#76aa2e;
  --dark:#222222;
  --darker:#1b1b1b;
  --team-bg:#1f1f1f;
  --text:#555555;
  --muted:#888888;
  --light:#f4f4f4;
  --white:#ffffff;
}
*{margin:0;padding:0;box-sizing:border-box}
html,body{width:1200px;height:3319px;overflow:hidden}
body{font-family:"Open Sans",Arial,sans-serif;color:var(--text);background:var(--white);position:relative}
.abs{position:absolute}
.topbar{left:0;top:0;width:1200px;height:23px;background:var(--dark);color:#ddd;font-size:12px}
.topbar .phone{left:200px;top:3px;display:flex;align-items:center;gap:8px}
.topbar .search{left:830px;top:4px;width:185px;height:16px;background:#555;border-radius:2px;color:#aaa;font-size:10px;padding:1px 8px}
.navbar{left:0;top:23px;width:1200px;height:67px;background:var(--green)}
.brand{left:180px;top:17px;color:var(--white);font-size:28px;font-weight:600;display:flex;align-items:center;gap:8px}
.brand .mark{width:16px;height:16px;background:var(--white)}
.nav{left:715px;top:24px;display:flex;gap:30px;color:var(--white);font-size:14px;font-weight:600}
.hero{left:0;top:90px;width:1200px;height:350px;background:linear-gradient(180deg,#6f9fcf 0%,#a9c4dd 45%,#8a7f6c 65%,#5f5042 100%)}
.tagline{left:608px;top:110px;width:413px;height:40px;background:rgba(40,40,40,.85);color:var(--white);font-size:16px;display:flex;align-items:center;justify-content:center}
.welcome h1{left:0;top:518px;width:1200px;text-align:center;font-size:27px;font-weight:600;color:#222;letter-spacing:.5px}
.welcome h1 span{color:var(--green)}
.welcome .lead{left:0;top:572px;width:1200px;text-align:center;font-size:14px;color:var(--muted)}
.feature{width:250px;text-align:center;top:664px}
.feature svg{display:block;margin:0 auto}
.feature h3{font-size:16px;font-weight:600;color:#333;margin-top:8px}
.feature p{font-size:11.5px;line-height:16px;color:#666;margin-top:14px}
.whatwedo{left:0;top:876px;width:1200px;height:610px;background:linear-gradient(180deg,#6d6d6d 0%,#4a4a4a 40%,#2d2a28 75%,#4a3a26 100%)}
.whatwedo h2{left:0;top:940px;width:1200px;text-align:center;font-size:27px;font-weight:600;color:var(--white)}
.whatwedo .lead{left:0;top:988px;width:1200px;text-align:center;font-size:13px;line-height:20px;color:#eee}
.tower{left:212px;top:1070px;width:337px;height:332px;background:linear-gradient(180deg,#c8dcef 0%,#9fc0e0 60%,#7f8f6a 100%)}
.accordion{left:613px;top:1070px;width:416px}
.acc-open{background:rgba(255,255,255,.85);height:173px}
.acc-head{height:30px;background:#e6e6e6;display:flex;align-items:center;font-size:12px;color:#333}
.acc-head .sign{width:30px;height:30px;display:flex;align-items:center;justify-content:center;font-weight:700;color:#555}
.acc-open .sign{background:var(--green);color:var(--white)}
.acc-body{padding:14px 18px;font-size:11.5px;line-height:16px;color:#666}
.acc-item{margin-top:11px;height:27px;background:#eee;display:flex;align-items:center;font-size:12px;color:#333}
.acc-item .sign{width:30px;text-align:center;font-weight:700}
.projects h2{left:0;top:1548px;width:1200px;text-align:center;font-size:27px;color:#222}
.projects .lead{left:0;top:1600px;width:1200px;text-align:center;font-size:13px;color:var(--muted)}
.card{top:1677px;width:197px;text-align:center;border-bottom:1px solid #ddd;height:223px}
.card .ph{height:128px}
.card h4{font-size:14px;font-weight:600;color:#333;margin-top:18px;line-height:18px}
.card .cat{font-size:13px;color:var(--muted);margin-top:12px}
.arrows{display:flex;gap:4px}
.arrows span{width:22px;height:22px;background:var(--green);display:flex;align-items:center;justify-content:center}
.team{left:0;top:1976px;width:1200px;height:603px;background:var(--team-bg)}
.team h2{left:0;top:2018px;width:1200px;text-align:center;font-size:27px;color:var(--white)}
.team .lead{left:0;top:2075px;width:1200px;text-align:center;font-size:13px;line-height:21px;color:#ccc}
.member{top:2147px;width:197px;text-align:center}
.member .ph{height:199px;background:linear-gradient(180deg,#8a8f94 0%,#b89a86 55%,#5a6b80 100%)}
.member h4{font-size:12px;font-weight:700;color:var(--white);margin-top:16px}
.member .role{font-size:10px;color:#999;margin-top:2px}
.member p{font-size:10.5px;line-height:14px;color:#999;margin-top:9px}
.partners h2{left:0;top:2638px;width:1200px;text-align:center;font-size:27px;color:#222}
.partners .lead{left:0;top:2688px;width:1200px;text-align:center;font-size:13px;line-height:20px;color:var(--muted)}
.badges{left:175px;top:2780px;width:850px;display:flex;justify-content:space-between;align-items:center}
.badge{width:100px;height:36px;background:#d9d9d9;border-radius:3px}
.footer{left:0;top:2954px;width:1200px;height:365px;background:var(--dark);color:#bbb}
.fcol{top:2990px;width:195px}
.fcol h5{font-size:14px;font-weight:600;color:var(--white);padding-bottom:10px;border-bottom:1px solid #444}
.fcol p{font-size:11px;line-height:16px;margin-top:18px}
.ci{display:flex;gap:10px;font-size:11px;line-height:16px;margin-top:18px}
.field{background:#3a3a3a;height:24px;font-size:10px;color:#999;padding:5px 8px}
.btn{background:var(--green);color:var(--white);font-size:10px;font-weight:600;display:flex;align-items:center;justify-content:center}
.copyright{left:190px;top:3277px;font-size:11px;color:#999}
.social{left:858px;top:3226px;display:flex;gap:14px}
.social span{width:12px;height:12px;border-radius:50%;background:#999}
.fdivider{left:174px;top:3255px;width:852px;height:1px;background:#3a3a3a}
</style>
</head>
<body>

<div class="abs topbar">
  <div class="abs phone">
    <svg width="12" height="12" viewBox="0 0 24 24"><path d="M6 2l4 4-2 3c1 3 4 6 7 7l3-2 4 4-3 4C10 22 2 14 2 5z" fill="var(--green)"/></svg>
    1-800-555-0142
  </div>
  <div class="abs search">Search...</div>
</div>

<div class="abs navbar">
  <div class="abs brand"><span class="mark"></span>Velnar Networks</div>
  <nav class="abs nav"><span>Velnar About Us</span><span>Velnar Contact Us</span><span>Velnar Blog</span></nav>
</div>

<div class="abs hero" role="img" aria-label="Wireless dish and camera mounted on a pole above a mountain valley town"></div>
<div class="abs tagline">All Your Wireless Needs A Professional Solution</div>

<section class="welcome">
  <h1 class="abs">WELCOME TO <span>VELNARNETWORKS</span></h1>
  <p class="abs lead">Our focus is to provide creative solutions paired with unparalleled technical and customer support.</p>
  <div class="abs feature" style="left:186px">
    <svg width="36" height="36" viewBox="0 0 36 36"><path d="M6 6l24 24M30 6L6 30" stroke="#222" stroke-width="5" stroke-linecap="round"/></svg>
    <h3>Services</h3>
    <p>Providing world class services is Velnar Network's commitment. We provide a whole host of services from installation to design work.</p>
  </div>
  <div class="abs feature" style="left:472px">
    <svg width="36" height="36" viewBox="0 0 36 36"><circle cx="16" cy="20" r="9" fill="none" stroke="#222" stroke-width="6" stroke-dasharray="4 3"/><circle cx="28" cy="8" r="5" fill="none" stroke="#222" stroke-width="4"/></svg>
    <h3>Solution</h3>
    <p>We are a vendor neutral solution provider. We carefully learn the needs of our customers and fit them with the right solution.</p>
  </div>
  <div class="abs feature" style="left:763px">
    <svg width="36" height="36" viewBox="0 0 36 36"><path d="M8 28L28 8M8 8l20 20" stroke="#222" stroke-width="5"/><rect x="4" y="26" width="6" height="6" fill="#222"/></svg>
    <h3>Design</h3>
    <p>Designing networks is a combination of science, standards and a little bit of art. Many IT companies can sell you the equipment, but we not only sell it, we understand it, and will guarantee it will work.</p>
  </div>
</section>

<section class="abs whatwedo" role="img" aria-label="Town lights at dusk beneath a communications tower"></section>
<h2 class="abs" style="left:0;top:940px;width:1200px;text-align:center;font-size:27px;font-weight:600;color:#fff">WHAT WE DO</h2>
<p class="abs" style="left:0;top:988px;width:1200px;text-align:center;font-size:13px;line-height:20px;color:#eee">We live in a digital world that is connected. We are here to make those connections, and help our customers succeed.<br>Whatever your IT need or goal is, we will strive to meet and exceed your expectations.</p>
<div class="abs tower" role="img" aria-label="Lattice communications tower under blue sky"></div>
<div class="abs accordion">
  <div class="acc-open">
    <div class="acc-head"><span class="sign">−</span>Our Solutions</div>
    <div class="acc-body">We provide consulting, design, regulatory knowledge, installation, repair, tower climbing, data/voice/video cabling, wireless networking, switches, routers, project management and complete managed services.</div>
  </div>
  <div class="acc-item"><span class="sign">+</span>Customer Focus</div>
  <div class="acc-item"><span class="sign">+</span>Safety First</div>
  <div class="acc-item"><span class="sign">+</span>Professionalism</div>
  <div class="acc-item"><span class="sign">+</span>Quality</div>
</div>

<section class="projects">
  <h2 class="abs">OUR LATEST PROJECTS</h2>
  <p class="abs lead">Take a look at our latest projects and learn more about what we can do for you and your networking needs.</p>
  <div class="abs card" style="left:174px"><div class="ph" role="img" aria-label="Point-to-point dish on a rooftop mast" style="background:linear-gradient(180deg,#b9d3ea,#8e9a8a)"></div><h4>Skyreach Q16 1.6 Gbps</h4><div class="cat">Point-to-Point</div></div>
  <div class="abs card" style="left:393px"><div class="ph" role="img" aria-label="Flat panel antenna in a lumber yard" style="background:linear-gradient(180deg,#5f9ad6,#c9c9c9)"></div><h4>Wireless Solution Lumber Yard</h4><div class="cat">Indoor-Wireless</div></div>
  <div class="abs card" style="left:613px"><div class="ph" role="img" aria-label="Radio units mounted on a rooftop pole" style="background:linear-gradient(180deg,#a8c6e4,#9a9a8a)"></div><h4>Linkstar L80 / Arcway P650</h4><div class="cat">Point-to-Point</div></div>
  <div class="abs card" style="left:830px"><div class="ph" role="img" aria-label="Two white millimeter wave radios on a mast" style="background:linear-gradient(180deg,#d9dde2,#8f949a)"></div><h4>Dual Linkstar L80 Links</h4><div class="cat">Point-to-Point</div></div>
  <div class="abs arrows" style="left:575px;top:1922px">
    <span><svg width="8" height="8" viewBox="0 0 8 8"><path d="M6 0L2 4l4 4" fill="none" stroke="#fff" stroke-width="1.6"/></svg></span>
    <span><svg width="8" height="8" viewBox="0 0 8 8"><path d="M2 0l4 4-4 4" fill="none" stroke="#fff" stroke-width="1.6"/></svg></span>
  </div>
</section>

<section class="abs team"></section>
<h2 class="abs" style="left:0;top:2018px;width:1200px;text-align:center;font-size:27px;color:#fff">MEET OUR AMAZING TEAM</h2>
<p class="abs" style="left:0;top:2075px;width:1200px;text-align:center;font-size:13px;line-height:21px;color:#ccc">Experience is what drives our team. With our combination of experience and knowledge, we can solve your problems<br>and provide you with knowledge to help you make decisions.</p>
<div class="abs member" style="left:174px"><div class="ph" role="img" aria-label="Portrait of Mark Ellison"></div><h4>MARK ELLISON</h4><div class="role">CEO/Founder</div><p>Mark Ellison has 24+ years of experience in the data networking industry.</p></div>
<div class="abs member" style="left:393px"><div class="ph" role="img" aria-label="Portrait of Ryan Castell"></div><h4>RYAN CASTELL</h4><div class="role">VP of Sales and Marketing</div><p>Ryan Castell has 12+ years experience in sales in wireless networking.</p></div>
<div class="abs member" style="left:613px"><div class="ph" role="img" aria-label="Portrait of Dale Porter"></div><h4>DALE PORTER</h4><div class="role">Sales Executive</div><p>Dale Porter has 38+ years experience in sales and customer service.</p></div>
<div class="abs member" style="left:830px"><div class="ph" role="img" aria-label="Portrait of TJ Harlow"></div><h4>TJ HARLOW</h4><div class="role">System Engineer</div><p>TJ has 6+ years experience in desktop support and network engineering.</p></div>
<div class="abs arrows" style="left:575px;top:2514px">
  <span><svg width="8" height="8" viewBox="0 0 8 8"><path d="M6 0L2 4l4 4" fill="none" stroke="#fff" stroke-width="1.6"/></svg></span>
  <span><svg width="8" height="8" viewBox="0 0 8 8"><path d="M2 0l4 4-4 4" fill="none" stroke="#fff" stroke-width="1.6"/></svg></span>
</div>

<section class="partners">
  <h2 class="abs">OUR PARTNERS</h2>
  <p class="abs lead">Velnar Networks partners with the market leaders in networking technologies. We are committed to delivering<br>the right product for your need, everytime.</p>
  <div class="abs badges">
    <span class="badge"></span><span class="badge"></span><span class="badge"></span><span class="badge"></span><span class="badge"></span><span class="badge"></span>
  </div>
  <div class="abs arrows" style="left:575px;top:2859px">
    <span><svg width="8" height="8" viewBox="0 0 8 8"><path d="M6 0L2 4l4 4" fill="none" stroke="#fff" stroke-width="1.6"/></svg></span>
    <span><svg width="8" height="8" viewBox="0 0 8 8"><path d="M2 0l4 4-4 4" fill="none" stroke="#fff" stroke-width="1.6"/></svg></span>
  </div>
</section>

<footer class="abs footer"></footer>
<div class="abs fcol" style="left:174px;color:#bbb">
  <h5>About Us</h5>
  <p>In 2008, Mark and Brian Salter along with Ryan Castell and the Ridgeline network team launched Velnar Networks through the acquisition of Ridgeline's network integration operations to utilize their extensive experience to help companies start, build, and maintain their own wireless infrastructure.</p>
</div>
<div class="abs fcol" style="left:393px;color:#bbb">
  <h5>Contact Us</h5>
  <div class="ci"><svg width="10" height="14" viewBox="0 0 10 14"><path d="M5 0a5 5 0 015 5c0 4-5 9-5 9S0 9 0 5a5 5 0 015-5z" fill="#bbb"/></svg><span>4210 W Prairie Road<br>Loveland, CO 80537</span></div>
  <div class="ci"><svg width="10" height="12" viewBox="0 0 24 24"><path d="M6 2l4 4-2 3c1 3 4 6 7 7l3-2 4 4-3 4C10 22 2 14 2 5z" fill="#bbb"/></svg><span>970-555-0188</span></div>
  <div class="ci"><svg width="12" height="10" viewBox="0 0 12 10"><rect width="12" height="10" fill="#bbb"/><path d="M0 0l6 5 6-5" fill="none" stroke="#222"/></svg><span>sales@velnarnetworks.com</span></div>
</div>
<div class="abs fcol" style="left:613px">
  <h5>Quick Contact</h5>
  <div style="display:flex;gap:6px;margin-top:18px"><div class="field" style="width:95px">Name...</div><div class="field" style="width:95px">Email...</div></div>
  <div class="field" style="margin-top:6px">Subject...</div>
  <div class="field" style="margin-top:6px;height:70px">Message...</div>
  <div class="btn" style="width:62px;height:24px;margin:6px 0 0 133px">SUBMIT</div>
</div>
<div class="abs fcol" style="left:830px">
  <h5>Newsletter</h5>
  <p style="margin-top:18px">Subscribe to Our Newsletter</p>
  <div style="display:flex;gap:4px;margin-top:8px"><div class="field" style="width:125px">Email...</div><div class="btn" style="width:66px;height:24px">SUBSCRIBE</div></div>
</div>
<div class="abs fdivider"></div>
<div class="abs social"><span></span><span></span><span></span><span></span><span></span></div>
<div class="abs copyright">Copyright © 2014 Velnar Networks, Inc. All Rights Reserved.</div>

</body>
</html>
```